Sehr angenehme und professionelle Zusammenarbeit!
Zielgruppe
Ich bin ein Consultant, der sich jetzt selbständig macht. Alles weitere steht in meinen Briefing. Dort findet ihr Fotos, mein Logo und damit auch die Farben, die ich mir wünsche. Meine Zielgruppe sind überwiegend Firmen, aber auch deren Mitarbeitende.
Aufgabenstellung
Die Struktur habe ich versucht zu beschreiben und hoffentlich auch alles über mich und mein Business. Ich freue mich auf eure kreativen und individuellen Vorschläge und bemühe mich zeitnah Feedback zu geben. Manchmal kann es den einen oder anderen Tag dauern. Bei Fragen gerne melden. Ich werde die Fragen, die für alle relevant sind auch im allgemeinen Kommentarfeld veröffentlichen.

```html
<!DOCTYPE html>
<html lang="de">
<head>
<meta charset="utf-8">
<title>Ihr Nutzen</title>
<link rel="stylesheet" href="https://fonts.googleapis.com/css2?family=Montserrat:wght@400;500;600;700&display=swap">
<style>
:root{
  --bg-soft:#f6f8fc;
  --white:#ffffff;
  --navy:#0d3f8c;
  --indigo:#2a2577;
  --accent:#3d7dd0;
  --text:#555a63;
  --note:#b9bcc4;
  --tab-1:#b3c3de;
  --tab-2:#c5d7f2;
  --panel-a:#dce7fb;
  --panel-b:#e4eefd;
  --panel-c:#cfdefd;
}
*{margin:0;padding:0;box-sizing:border-box}
html,body{width:1200px;height:2574px;overflow:hidden;background:var(--white)}
body{position:relative;font-family:"Montserrat",sans-serif;color:var(--text)}
.abs{position:absolute}
.section{position:absolute;left:0;width:1200px;background:var(--bg-soft)}
.eyebrow{position:absolute;left:159px;font-size:12px;font-weight:700;letter-spacing:1.6px;color:var(--accent)}
.headline{position:absolute;left:159px;font-size:23px;font-weight:500;color:var(--navy)}
.copy{position:absolute;font-size:10.1px;line-height:18.8px;color:var(--text)}
.copy p+p{margin-top:18.8px}
.note{position:absolute;font-size:9px;line-height:15px;color:var(--note);text-align:center}
.tabs{position:absolute;left:159px;top:418px;width:580px;height:42px;display:flex}
.tab{flex:1;display:flex;align-items:center;justify-content:center;font-size:11px;color:#eef2fa;letter-spacing:.3px}
.tab--staff{background:var(--tab-1)}
.tab--lead{background:var(--tab-2)}
.tab--org{background:var(--indigo);font-weight:700;color:var(--white)}
.tab-body{position:absolute;left:159px;top:460px;width:580px;height:330px;background:var(--white)}
.brand-disc{position:absolute;border-radius:50%;background:var(--white);display:flex;align-items:center;justify-content:center;gap:8px;font-size:15px;font-weight:600;color:var(--navy)}
.brand-dot{width:12px;height:12px;border-radius:50%;background:var(--accent)}
.wheel{position:absolute;left:0;top:1672px;width:600px;height:675px}
.wheel-label{position:absolute;font-size:13.5px;color:var(--navy);letter-spacing:.3px}
.wheel-label--active{font-weight:700;border-bottom:2px solid var(--navy);padding-bottom:1px}
.detail-title{position:absolute;left:694px;top:1820px;font-size:14.5px;font-weight:700;color:var(--navy)}
.pager{position:absolute;top:2167px;width:31px;height:31px;border:1px solid var(--accent);border-radius:50%;display:flex;align-items:center;justify-content:center}
.cta{position:absolute;left:891px;top:2167px;width:157px;height:31px;border:1px solid var(--navy);font-size:9px;font-weight:500;color:var(--navy);display:flex;align-items:center;justify-content:center}
</style>
</head>
<body>

<section class="section" style="top:0;height:898px">
  <div class="eyebrow" style="top:95px">IHR NUTZEN:</div>
  <h2 class="headline" style="top:117px">Von Lose zu Win für alle Seiten</h2>
  <div class="copy" style="left:159px;top:167px;width:585px">
    <p>Während auf individueller Ebene Menschen ihr Potenzial nicht entfalten können und oft lange an der Situation leiden, entstehen auf organisationaler Ebene wirtschaftliche Einbußen und Imageschäden. Selten ist nur eine Person betroffen, auch wenn es sich oft auf eine Person fokussiert. Die Ursachen sind multifaktoriell und langwierig, die negative Wirkung strahlt auf den/die Mitarbeitende/n, die Führungskraft, das Team und die Abteilung aus.</p>
    <p>Für alle. Das Beste. Bedeutet nicht, dass alle Beteiligten ihre optimale Wunschvorstellung erfüllen. Es bedeutet, dass wir die bestmögliche Lösung erarbeiten, in die alle Sichtweisen einfließen, Wahlmöglichkeiten bestehen und eine dysfunktionale Situation nachhaltig aufgelöst wird. Und letztendlich sogar Entwicklungschancen entstehen. „Boost or Leave“ – es gibt immer diese beiden Möglichkeiten. Entweder eine echte Entwicklung, an der alle beteiligt sind, oder ein Verlassen der Situation, das gemeinsam entschieden wird.</p>
  </div>

  <div class="note" style="left:37px;top:435px">( auf Tabs klicken)</div>
  <div class="tabs">
    <div class="tab tab--staff">MITARBEITENDE/R</div>
    <div class="tab tab--lead">FÜHRUNGSKRAFT</div>
    <div class="tab tab--org">ORGANISATION</div>
  </div>
  <div class="tab-body">
    <div class="copy" style="left:50px;top:42px;width:460px">
      <p>Eine Konfliktsituation bleibt nie auf eine Person beschränkt. Neben wirtschaftlichen Einbußen für die Organisation, verursacht durch Fehlzeiten, Ausfälle und Nichterreichung von Zielen, gibt es fast immer einen Imageschaden. Spannungen breiten sich über das Team hinaus aus, Gerüchte brodeln, Ungerechtigkeitsdiskussionen finden statt, das Vertrauen in die Führung leidet, Verunsicherung ist spürbar.</p>
      <p>In meinem Beratungsprozess loten wir aus, welche internen Lösungen machbar sind, besprechen transparente und nachvollziehbare Kommunikationsmöglichkeiten. So können komplexe Personalsituationen und deren Lösung dazu beitragen, Ihr Unternehmen als lernende Organisation zu entwickeln. Eine schwierige Situation kann zu einer Entwicklungschance werden.</p>
    </div>
  </div>

  <div class="brand-disc" style="left:815px;top:482px;width:226px;height:226px"><span class="brand-dot"></span>Markenname</div>
</section>

<section class="section" style="top:943px;height:587px">
  <div class="eyebrow" style="top:95px">IHR NUTZEN:</div>
  <h2 class="headline" style="top:117px">Von Lose zu Win für alle Seiten</h2>
  <div class="copy" style="left:159px;top:167px;width:505px">
    <p>Während auf individueller Ebene Menschen ihr Potenzial nicht entfalten können und oft lange an der Situation leiden, entstehen auf organisationaler Ebene wirtschaftliche Einbußen und Imageschäden. Selten ist nur eine Person betroffen, auch wenn es sich oft auf eine Person fokussiert. Die Ursachen sind multifaktoriell und langwierig, die negative Wirkung strahlt auf den/ die Mitarbeitende/n, die Führungskraft, das Team und die Abteilung aus.</p>
    <p>Für alle. Das Beste. Bedeutet nicht, dass alle Beteiligten ihre optimale Wunschvorstellung erfüllen. Es bedeutet, dass wir die bestmögliche Lösung erarbeiten, in die alle Sichtweisen einfließen, Wahlmöglichkeiten bestehen und eine dysfunktionale Situation nachhaltig aufgelöst wird. Und letztendlich sogar Entwicklungschancen entstehen. „Boost or Leave“ – es gibt immer diese beiden Möglichkeiten. Entweder eine echte Entwicklung, an der alle beteiligt sind, oder ein Verlassen der Situation, das gemeinsam entschieden wird.</p>
  </div>
  <div class="note" style="left:163px;top:425px;text-align:left">(Positionen der Popup im Prototype nicht perfekt)</div>
  <div class="note" style="left:838px;top:96px;width:160px">( Hover funktioniert bei Prototyp nicht deswegen klicken)</div>
  <div class="brand-disc" style="left:801px;top:140px;width:240px;height:240px"><span class="brand-dot"></span>Markenname</div>
</section>

<div class="wheel">
  <svg class="abs" style="left:0;top:0" width="600" height="675" viewBox="0 0 600 675" aria-hidden="true">
    <rect width="600" height="675" fill="var(--panel-c)"/>
    <polygon points="0,0 300,0 300,338 0,508" fill="var(--panel-a)"/>
    <polygon points="300,0 600,0 600,508 300,338" fill="var(--panel-b)"/>
    <circle cx="300" cy="338" r="126" fill="var(--white)"/>
  </svg>
  <div class="brand-disc" style="left:174px;top:212px;width:252px;height:252px;background:transparent"><span class="brand-dot"></span>Markenname</div>
  <div class="note" style="left:232px;top:30px;width:160px">( Hover funktioniert bei Prototyp nicht deswegen klicken)</div>
  <div class="wheel-label wheel-label--active" style="left:85px;top:158px">MITARBEITENDE/R</div>
  <div class="wheel-label" style="left:388px;top:150px">FÜHRUNGSKRAFT</div>
  <div class="wheel-label" style="left:247px;top:509px">ORGANISATION</div>
</div>

<h3 class="detail-title">Mitarbeitende/r</h3>
<div class="copy" style="left:694px;top:1859px;width:360px">
  <p>Oft beginnt es mit Unzufriedenheit, vielleicht fehlender Wertschätzung oder Überlastung und einem angeknacksten Vertrauen in sich selbst, in die Führungskraft oder Organisation. In einer andauernden Konfliktsituation kommen später physische und psychische Belastungssymptome, mitunter Fehlzeiten hinzu.</p>
  <p>In den Beratungsterminen berücksichtigen wir gemeinsam Ihre Persönlichkeitsmerkmale, Erfolgs- und Misserfolgsgeschichten, das Unternehmensumfeld und Ihre persönlichen Umstände. Um zu verstehen, wie die Situation entstehen konnte und um neue Lösungswege auszumachen. Oft lässt sich herausfinden, was die Tätigkeit und wo der Platz ist, in der Sie beziehungsweise an dem Sie gut wirken können. Manchmal ist es ein mutiges Vorwärts zu etwas Neuem. Manchmal ist es ein mutiges Rückwärts zu Ihren Wurzeln. Aber es bleibt Ihre Wahl.</p>
</div>
<div class="pager" style="left:694px" aria-label="zurück"><svg width="10" height="10" viewBox="0 0 10 10"><path d="M6.5 1.5 3 5l3.5 3.5" fill="none" stroke="var(--navy)" stroke-width="1"/></svg></div>
<div class="pager" style="left:734px" aria-label="weiter"><svg width="10" height="10" viewBox="0 0 10 10"><path d="M3.5 1.5 7 5 3.5 8.5" fill="none" stroke="var(--navy)" stroke-width="1"/></svg></div>
<div class="cta">Zum Kennenlerngespräch</div>

</body>
</html>
```